Ecommerce Web Design - We currently have a live website running on https://www.plovenrik.co.za - this website must be redesigned for an eCommerce website since we are moving to sell our items online. Kindly put a new design utilising the information from the current live website

Link to Pictures & Brochure: https://dostravel-files.example.com/:f:/g/personal/tavimo_rushe_co_za/QxxLPTmvdJaUkrBWa7TYzpfnC-KLM9dHWuqTXCB4jLNUwe?e=qR5m31

```html
<!DOCTYPE html>
<html lang="en">
<head>
<meta charset="utf-8">
<title>PLOVENRIK – Fibreglass Ladders Online Store</title>
<link href="https://fonts.googleapis.com/css2?family=Jost:wght@400;500;600;700&family=Montserrat:wght@800&family=Poppins:wght@400;500;600&display=swap" rel="stylesheet">
<style>
:root{
  --navy:#1c2a45;
  --blue:#1f5bb4;
  --blue-dark:#163f85;
  --orange:#f58634;
  --text:#2b3445;
  --muted:#8a93a3;
  --line:#e6e9ef;
  --panel:#f1f3f7;
  --cream:#fdf4e8;
  --white:#ffffff;
}
*{box-sizing:border-box;margin:0;padding:0}
html,body{width:1200px;height:4483px;overflow:hidden}
body{position:relative;background:var(--white);font-family:"Poppins",sans-serif;color:var(--text);font-size:12px}
.abs{position:absolute}
.heading{font-family:"Jost",sans-serif;color:var(--blue);font-weight:600;text-align:center;position:absolute;left:0;width:1200px}
.stars{color:var(--orange);letter-spacing:1px;font-size:12px}
.img{border-radius:2px}

/* header */
.logo{left:92px;top:14px;display:flex;align-items:center;gap:8px}
.logo-mark{width:24px;height:24px;background:var(--blue)}
.logo-name{font-family:"Jost",sans-serif;font-weight:700;font-size:16px;color:var(--blue)}
.search{left:258px;top:24px;width:418px;height:36px;border-radius:18px;background:var(--panel);padding:0 18px;display:flex;align-items:center;justify-content:space-between;color:var(--muted);font-size:12px}
.locale{left:826px;top:34px;font-size:11px;color:var(--muted);display:flex;gap:22px}
.icons{left:1002px;top:28px;display:flex;gap:26px}
.icon{width:20px;height:20px;position:relative}
.badge{position:absolute;right:-8px;top:-8px;width:14px;height:14px;border-radius:50%;background:var(--blue);color:#fff;font-size:8px;display:flex;align-items:center;justify-content:center}
.nav{left:0;top:84px;width:1200px;height:50px;border-top:1px solid var(--line);display:flex;align-items:center;padding:0 84px}
.nav a{font-family:"Jost",sans-serif;color:var(--blue);font-weight:500;font-size:13px;text-decoration:none;margin-right:30px}
.nav .advice{margin-left:auto;font-size:12px;color:var(--text)}

/* hero */
.hero{left:0;top:134px;width:1200px;height:516px;background:var(--navy)}
.hero h1{position:absolute;left:84px;top:96px;font-family:"Montserrat",sans-serif;font-weight:800;color:#fff;font-size:64px;line-height:66px;letter-spacing:1px}
.duty{left:88px;top:282px;color:#fff;font-size:11px;font-weight:500}
.ratings{left:92px;top:316px;display:flex;gap:12px}
.rating{width:58px;height:58px;border-radius:50%;border:3px solid #fff}
.volt{left:402px;top:312px;width:80px;text-align:center;color:#fff;font-size:8px;line-height:10px}
.btn-outline{left:88px;top:416px;width:148px;height:42px;border:2px solid #fff;border-radius:21px;color:#fff;font-family:"Jost",sans-serif;font-weight:600;font-size:13px;display:flex;align-items:center;justify-content:center;letter-spacing:.5px}

/* service band */
.band{left:0;top:650px;width:1200px;height:160px;background:var(--panel)}
.service{position:absolute;top:48px;display:flex;gap:16px}
.service .pic{width:58px;height:58px;border-radius:8px}
.service p{font-size:12px;font-weight:500;color:var(--text);margin:10px 0 12px}
.pill{display:inline-block;padding:6px 20px;border-radius:14px;color:#fff;font-size:9px;font-weight:600}

/* image cards */
.card3{top:884px;width:327px;height:208px}
.card3 span{position:absolute;left:24px;bottom:24px;color:#fff;font-family:"Jost",sans-serif;font-weight:600;font-size:24px;line-height:30px}

/* categories */
.cats{left:86px;top:1203px;display:flex;gap:6px}
.cat{width:201px;height:243px;background:var(--panel);position:relative;padding:26px 26px}
.cat h3{font-family:"Jost",sans-serif;color:var(--blue);font-weight:500;font-size:17px;line-height:23px}
.cat .more{display:inline-block;margin-top:10px;background:#fff;color:var(--blue);font-size:9px;padding:4px 16px;border-radius:10px}
.cat .pic{position:absolute;right:16px;bottom:14px;width:92px;height:96px}

/* products */
.products{left:84px;width:1032px;display:flex;border:1px solid var(--line)}
.prod{flex:1;border-right:1px solid var(--line);padding:12px 16px;position:relative}
.prod:last-child{border-right:0}
.prod .pic{width:150px;height:160px;margin:0 auto 18px}
.prod .name{font-size:11.5px;line-height:21px;color:var(--text);height:44px}
.prod .price{font-family:"Jost",sans-serif;font-size:16px;font-weight:600;margin:20px 0 8px}
.prod .price s{font-size:11px;color:var(--muted);font-weight:400;margin-left:4px}
.orange{color:var(--orange)}
.tag{position:absolute;left:16px;top:16px;font-size:8px;color:#fff;padding:2px 7px;border-radius:8px}
.tag.out{background:#c9ced6}
.tag.hot{background:#e8412c}
.tag.sale{background:var(--orange)}
.arrow{width:44px;height:44px;border-radius:50%;background:#e4e7ee;display:flex;align-items:center;justify-content:center}
.dots{left:590px;display:flex;gap:6px}
.dots i{width:7px;height:7px;border-radius:50%;background:#c9d5ea;display:block}
.dots i:first-child{background:var(--blue)}

/* brands */
.brands{left:100px;top:2000px;width:1000px;display:flex;justify-content:space-between;align-items:center}
.brand{width:130px;height:36px;display:flex;align-items:center;justify-content:center;font-family:"Jost",sans-serif;font-weight:700;font-size:16px;color:var(--blue-dark)}

/* deals */
.deal-title{left:316px;top:2116px;font-family:"Jost",sans-serif;color:var(--blue);font-weight:600;font-size:32px}
.timer{left:696px;top:2120px;display:flex;gap:4px;align-items:center}
.timer b{width:24px;height:32px;background:var(--orange);color:#fff;font-family:"Jost",sans-serif;font-size:20px;display:flex;align-items:center;justify-content:center;font-weight:500}
.timer em{font-style:normal;color:var(--orange);font-weight:700;font-size:18px}
.deals{top:2185px;height:375px;border:2px solid var(--orange)}
.off{position:absolute;left:16px;top:18px;width:40px;height:40px;border-radius:50%;background:var(--blue);color:#fff;font-size:13px;font-weight:500;display:flex;align-items:center;justify-content:center}
.stock{display:flex;align-items:center;gap:12px;margin-top:26px;font-size:8px;color:var(--muted);line-height:9px}
.stock b{font-family:"Jost",sans-serif;font-size:22px;color:var(--blue-dark);font-weight:600}

/* tabs */
.tabs{left:0;top:2686px;width:1200px;display:flex;justify-content:center;gap:34px;font-family:"Jost",sans-serif;font-size:18px;color:var(--blue)}
.tabs .active{font-weight:600;text-decoration:underline;text-underline-offset:4px}

/* promos */
.promo{top:3116px;width:505px;height:208px;padding:60px 26px;color:#fff}
.promo h4{font-family:"Jost",sans-serif;font-weight:600;font-size:24px;line-height:32px}
.promo .disc{font-family:"Jost",sans-serif;font-size:36px;color:var(--orange);font-weight:600;line-height:36px}
.promo .pill{background:var(--blue);margin-top:6px;font-size:11px}

/* reviews */
.reviews{left:0;top:3390px;width:1200px;height:416px;background:var(--cream);overflow:hidden}
.reviews h2{position:absolute;left:0;width:1200px;top:56px;text-align:center;font-family:"Jost",sans-serif;color:var(--blue);font-size:32px;font-weight:600}
.quote{display:inline-block;width:30px;height:24px;margin-right:14px}
.rev{position:absolute;top:110px;width:254px;background:#fff;padding:26px 24px;font-size:12.5px;line-height:22px;color:var(--text)}
.rev .who{font-family:"Jost",sans-serif;font-weight:600;color:var(--blue);font-size:14px;margin:14px 0 12px}

/* newsletter */
.news-title{top:3888px;font-size:34px;line-height:42px}
.news-form{left:392px;top:3982px;display:flex;gap:10px}
.news-form .field{width:282px;height:40px;border:1px solid var(--line);border-radius:20px;padding:0 20px;display:flex;align-items:center;font-size:12px;color:var(--muted)}
.news-form .go{width:124px;height:40px;border-radius:20px;background:var(--orange);color:#fff;font-weight:600;font-size:13px;display:flex;align-items:center;justify-content:center}
.env{position:absolute;border:2px solid #f3dfe0;opacity:.8}

/* perks */
.perks{left:84px;top:4100px;width:1032px;height:38px;background:var(--panel);display:flex}
.perks div{flex:1;display:flex;align-items:center;justify-content:center;gap:8px;font-size:12px;font-weight:500;color:var(--blue);border-right:2px solid #fff}
.perks div:last-child{border-right:0}

/* footer */
.foot h5{font-family:"Jost",sans-serif;color:var(--blue);font-size:14px;font-weight:600;margin-bottom:24px}
.foot li{list-style:none;font-size:12px;color:var(--muted);line-height:30px}
.addr{left:84px;top:4224px;font-size:12px;color:var(--muted);line-height:22px}
.addr u{font-size:10px}
.social{left:90px;top:4314px;display:flex;gap:22px}
.social i{width:12px;height:12px;border-radius:50%;background:var(--muted);display:block}
.phone{font-family:"Jost",sans-serif;color:var(--blue);font-size:22px;font-weight:500;display:flex;align-items:center;gap:10px}
.hours{font-size:10px;color:var(--muted);line-height:18px;margin:8px 0 0 32px}
.copy{left:84px;top:4448px;font-size:12px;color:var(--text)}
.pay{left:716px;top:4446px;display:flex;gap:14px;font-family:"Jost",sans-serif;font-weight:600;font-size:11px;color:var(--blue-dark)}
.totop{left:1156px;top:4438px;width:30px;height:30px;background:var(--panel);display:flex;align-items:center;justify-content:center}
</style>
</head>
<body>

<!-- header -->
<div class="abs logo"><span class="logo-mark"></span><span class="logo-name">PLOVENRIK</span></div>
<div class="abs search">Search for products
  <svg width="14" height="14" viewBox="0 0 14 14"><circle cx="6" cy="6" r="4.5" fill="none" stroke="#1f5bb4" stroke-width="2"/><path d="M9.5 9.5L13 13" stroke="#1f5bb4" stroke-width="2"/></svg>
</div>
<div class="abs locale"><span>English ⌄</span><span>USD ⌄</span></div>
<div class="abs icons">
  <svg class="icon" viewBox="0 0 20 20"><circle cx="10" cy="7" r="4" fill="none" stroke="#f58634" stroke-width="1.6"/><path d="M3 18c1-4 4-6 7-6s6 2 7 6" fill="none" stroke="#f58634" stroke-width="1.6"/></svg>
  <div class="icon"><svg width="20" height="20" viewBox="0 0 20 20"><path d="M10 17L3 10a4 4 0 016-5l1 1 1-1a4 4 0 016 5z" fill="none" stroke="#f58634" stroke-width="1.6"/></svg><span class="badge">3</span></div>
  <div class="icon"><svg width="20" height="20" viewBox="0 0 20 20"><path d="M2 3h3l2 10h9l2-7H6" fill="none" stroke="#f58634" stroke-width="1.6"/><circle cx="8" cy="17" r="1.4" fill="#f58634"/><circle cx="15" cy="17" r="1.4" fill="#f58634"/></svg><span class="badge">2</span></div>
</div>
<nav class="abs nav">
  <a>Home</a><a>Products ⌄</a><a>Company Profile</a><a>Safty &amp; Information</a><a>Download</a>
  <span class="advice">Need Professional Advice? 011 555 0192</span>
</nav>

<!-- hero -->
<section class="abs hero">
  <h1>FIBREGLASS<br>LADDERS</h1>
  <div class="abs duty">OUR DUTY RATINGS</div>
  <div class="abs ratings">
    <span class="rating" style="background:#e23a33"></span>
    <span class="rating" style="background:#f2b51c"></span>
    <span class="rating" style="background:#2fa6e0"></span>
    <span class="rating" style="background:#2b2f36"></span>
  </div>
  <div class="abs volt">
    <svg width="40" height="36" viewBox="0 0 40 36"><path d="M20 2L38 34H2z" fill="#f5a623"/><path d="M22 10l-6 13h5l-3 9 8-14h-5l3-8z" fill="#1c2a45"/></svg><br>DOES NOT CONDUCT ELECTRICITY
  </div>
  <div class="abs btn-outline">View Range</div>
  <div class="abs img" role="img" aria-label="Yellow, red and aluminium step ladders standing side by side" style="left:552px;top:70px;width:610px;height:420px;background:linear-gradient(100deg,#26355a 0%,#c9a22a 25%,#d6402f 55%,#b7bcc4 85%,#26355a 100%);opacity:.85"></div>
</section>

<!-- service band -->
<section class="abs band">
  <div class="service" style="left:88px"><div class="pic" role="img" aria-label="Delivery truck icon" style="background:linear-gradient(#dfe6f3,#b9c7e2)"></div>
    <div><p>WE DELIVER COUNTRY WIDE</p><span class="pill" style="background:var(--orange)">Enquire Now</span></div></div>
  <div class="service" style="left:480px"><div class="pic" role="img" aria-label="Discount tag icon" style="background:linear-gradient(#fde6a6,#f5b33b)"></div>
    <div><p>VIEW OUR SPECIAL OFFER</p><span class="pill" style="background:var(--navy)">View More</span></div></div>
  <div class="service" style="left:852px"><div class="pic" role="img" aria-label="Advice chat icon" style="background:linear-gradient(#dbe7fb,#9fb8e6)"></div>
    <div><p>FOR PROFFESSIONAL ADVICE</p><span class="pill" style="background:var(--navy)">Contact Us</span></div></div>
</section>

<!-- image cards -->
<div class="abs card3 img" role="img" aria-label="Worker falling from a ladder in a warehouse" style="left:84px;background:linear-gradient(135deg,#b89a62,#6d6250)"><span>Ladder Safety</span></div>
<div class="abs card3 img" role="img" aria-label="Row of step ladders in a showroom" style="left:436px;background:linear-gradient(135deg,#8c8f96,#3b3e45)"><span>Selecting The<br>Right Ladder</span></div>
<div class="abs card3 img" role="img" aria-label="Warehouse worker between shelves" style="left:789px;background:linear-gradient(135deg,#5e82b0,#2d4468)"><span>Product Catalogue</span></div>

<!-- categories -->
<div class="heading" style="top:1156px;font-size:18px">Check out the most popular categories</div>
<div class="abs cats">
  <div class="cat"><h3>Access<br>Equipment</h3><span class="more">More</span><div class="pic" role="img" aria-label="Scaffold tower" style="background:linear-gradient(#e2e5ea,#b3b9c2)"></div></div>
  <div class="cat"><h3>Aluminium<br>Ladders</h3><span class="more">More</span><div class="pic" role="img" aria-label="Aluminium step ladder" style="background:linear-gradient(#e2e5ea,#c2c7ce)"></div></div>
  <div class="cat"><h3>Castor Wheels</h3><span class="more">More</span><div class="pic" role="img" aria-label="Grey castor wheel" style="background:linear-gradient(#e2e5ea,#9ea4ad)"></div></div>
  <div class="cat"><h3>Fibreglass<br>Ladders</h3><span class="more">More</span><div class="pic" role="img" aria-label="Yellow fibreglass ladder" style="background:linear-gradient(#efe7cf,#e7b93a)"></div></div>
  <div class="cat"><h3>Ladder<br>Accessories</h3><span class="more">More</span><div class="pic" role="img" aria-label="Ladder foot accessory" style="background:linear-gradient(#e2e5ea,#c6cbd2)"></div></div>
</div>

<!-- latest products -->
<div class="heading" style="top:1522px;font-size:32px">Latest products</div>
<div class="abs products" style="top:1583px;height:314px">
  <div class="prod"><span class="tag out">SOLD OUT</span><div class="pic" role="img" aria-label="Scaffold tower" style="background:linear-gradient(#eef0f3,#c3c8cf)"></div><div class="name">Digital Thermometer X30-Pro</div><div class="price orange">$77.65<s>$80.65</s></div><div class="stars">★★★★★</div></div>
  <div class="prod"><div class="pic" role="img" aria-label="Yellow scaffold frame" style="background:linear-gradient(#fbf3d6,#f0d064)"></div><div class="name">Karvel Sonic X500 Basic</div><div class="price orange">$38.39<s>$53.99</s></div><div class="stars">★★★★★</div></div>
  <div class="prod"><span class="tag hot">HOT</span><div class="pic" role="img" aria-label="Blue mobile platform ladder" style="background:linear-gradient(#e6f1fb,#3f9bd3)"></div><div class="name">Karvel Sonic X2000 Pro Black</div><div class="price">$299.99</div><div class="stars">★★★★★</div></div>
  <div class="prod"><div class="pic" role="img" aria-label="Aluminium step ladder" style="background:linear-gradient(#f0f1f3,#a9afb8)"></div><div class="name">Karvel Sonic X2500 Pro White</div><div class="price">$39.99</div><div class="stars">★★★★★</div></div>
  <div class="prod"><span class="tag out">SOLD OUT</span><div class="pic" role="img" aria-label="Grey castor wheel" style="background:linear-gradient(#eceef1,#8f959e)"></div><div class="name">GAnti-Dust Filter, Breathable, 3 Layers of Purifying</div><div class="price">$17.99</div><div class="stars">★★★★★</div></div>
</div>
<div class="abs arrow" style="left:60px;top:1716px"><svg width="10" height="14"><path d="M8 1L2 7l6 6" fill="none" stroke="#fff" stroke-width="2"/></svg></div>
<div class="abs arrow" style="left:1096px;top:1716px"><svg width="10" height="14"><path d="M2 1l6 6-6 6" fill="none" stroke="#fff" stroke-width="2"/></svg></div>
<div class="abs dots" style="top:1927px"><i></i><i></i></div>

<!-- brands -->
<div class="abs brands">
  <span class="brand">Ascendo</span><span class="brand">Featherline</span><span class="brand">Marvel Rungs</span><span class="brand">Grippa</span><span class="brand">Rollmark</span><span class="brand">Flexroll</span>
</div>

<!-- best deals -->
<div class="abs deal-title">Best Deals of the week!</div>
<div class="abs timer"><b>1</b><b>1</b><em>:</em><b>5</b><b>6</b><em>:</em><b>0</b><b>4</b></div>
<div class="abs products deals">
  <div class="prod"><span class="off">-26%</span><div class="pic" role="img" aria-label="Blue retractor hook" style="background:linear-gradient(#fff,#dde4ee)"></div><div class="name">Multi hook retractor surgical spinal retractors</div><div class="price orange">$65.39<s>$48.99</s></div><div class="stars">★★★★★</div><div class="stock"><span>No of pcs<br>available</span><b>3</b></div></div>
  <div class="prod"><span class="off">-54%</span><div class="pic" role="img" aria-label="Steel chain" style="background:linear-gradient(#fff,#dadde2)"></div><div class="name">3-Ply Ear-Loop Disposable Blue Face Mask</div><div class="price orange">$32.39<s>$14.99</s></div><div class="stars">★★★★★</div><div class="stock"><span>No of pcs<br>available</span><b>13</b></div></div>
  <div class="prod"><span class="off">-61%</span><div class="pic" role="img" aria-label="Stacked storage bins" style="background:linear-gradient(#fff,#5a4a42)"></div><div class="name">Disposable Face Mask for Unisex</div><div class="price orange">$20.39<s>$8.15</s></div><div class="stars">★★★★★</div><div class="stock"><span>No of pcs<br>available</span><b>10</b></div></div>
  <div class="prod"><span class="off">-30%</span><div class="pic" role="img" aria-label="Hand trolley" style="background:linear-gradient(#fff,#b7bcc4)"></div><div class="name">Blue Hot Water Bottle, 2 Quart Capacity</div><div class="price">$14.52 - $15.52</div><div class="stars">★★★★★</div><div class="stock"><span>No of pcs<br>available</span><b>22</b></div></div>
  <div class="prod"><div class="pic" role="img" aria-label="Flat platform trolley" style="background:linear-gradient(#fff,#c6cbd2)"></div><div class="name">Generic Stethoscope Hearing Heartbeat Tool</div><div class="price orange">$53.75<s>$38.24</s></div><div class="stars">★★★★★</div><div class="stock"><span>No of pcs<br>available</span><b>10</b></div></div>
</div>

<!-- top 5 -->
<div class="heading" style="top:2626px;font-size:32px">Top 5 Bestsellers in:</div>
<div class="abs tabs"><span class="active">Access Equipment</span><span>Aluminium Ladders</span><span>Castor Wheels</span></div>
<div class="abs products" style="top:2734px;height:314px">
  <div class="prod"><span class="tag out">SOLD OUT</span><div class="pic" role="img" aria-label="Scaffold tower" style="background:linear-gradient(#eef0f3,#c3c8cf)"></div><div class="name">Digital Thermometer X30-Pro</div><div class="price orange">$77.65<s>$80.65</s></div><div class="stars">★★★★★</div></div>
  <div class="prod"><span class="tag sale">SALE</span><span class="tag hot" style="top:34px">HOT</span><div class="pic" role="img" aria-label="Yellow scaffold frame" style="background:linear-gradient(#fbf3d6,#f0d064)"></div><div class="name">Automatic blood pressure monitor</div><div class="price orange">$90.65<s>$60.65</s></div><div class="stars">★★★★★</div></div>
  <div class="prod"><div class="pic" role="img" aria-label="Blue mobile platform ladder" style="background:linear-gradient(#e6f1fb,#3f9bd3)"></div><div class="name">Home Blood Pressure Monitors</div><div class="price orange">$90.65<s>$60.65</s></div><div class="stars">★★★★★</div></div>
  <div class="prod"><div class="pic" role="img" aria-label="Aluminium step ladder" style="background:linear-gradient(#f0f1f3,#a9afb8)"></div><div class="name">Blood Pressure Monitor with Stroke Risk Detection</div><div class="price orange">$77.65<s>$80.65</s></div><div class="stars">★★★★★</div></div>
  <div class="prod"><span class="tag out">SOLD OUT</span><div class="pic" role="img" aria-label="Aluminium step ladder" style="background:linear-gradient(#f0f1f3,#b5bac2)"></div><div class="name">Digital Thermometer X30-Pro</div><div class="price orange">$60.39<s>$89.99</s></div><div class="stars">★★★★★</div></div>
</div>

<!-- promos -->
<div class="abs promo img" role="img" aria-label="Workers in hard hats checking stock" style="left:84px;background:linear-gradient(90deg,#5b4a3a,#a98a6a 60%,#c7a27a)">
  <span class="pill" style="background:#2fae5b;padding:2px 8px;font-size:8px">NEW</span>
  <h4>Get best quality<br>at cheap price</h4><span class="pill">More</span>
</div>
<div class="abs promo img" role="img" aria-label="Courier carrying a box in a warehouse" style="left:612px;background:linear-gradient(90deg,#2a2a30,#6d5a4c 60%,#a88c72)">
  <h4 style="margin-top:-14px">Bright<br>Whitening Kit</h4><div class="disc">-10%</div><span class="pill">Shop now</span>
</div>

<!-- reviews -->
<section class="abs reviews">
  <h2><svg class="quote" viewBox="0 0 30 24"><path d="M6 2h8L8 22H0zM22 2h8l-6 20h-8z" fill="#f58634"/></svg>Latest reviews</h2>
  <div class="rev" style="left:-90px">There was a small mistake in the order. In return, I got the correct order and I could keep the wrong one for myself.<div class="who">Jory Calloway</div></div>
  <div class="rev" style="left:192px">I ordered on Friday evening and on Monday at 12:30 the package was with me. I have never encountered such a fast order processing.<div class="who">Tomas Reddin</div><div class="stars">★★★★★</div></div>
  <div class="rev" style="left:472px">I ordered on Friday evening and on Monday at 12:30 the package was with me. I have never encountered such a fast order processing.<div class="who">Mira Vantell</div><div class="stars">★★★★★</div></div>
  <div class="rev" style="left:752px">Everything is perfect. I would recommend!<div class="who">Lena Okafer</div><div class="stars">★★★★★</div></div>
  <div class="rev" style="left:1032px">There was a small mistake in the order. In return, I got the correct order and I could keep the wrong one for myself.<div class="who">Jory Calloway</div><div class="stars">★★★★★</div></div>
  <div class="abs dots" style="top:386px;left:590px"><i></i><i></i></div>
</section>

<!-- newsletter -->
<div class="env" style="left:140px;top:3920px;width:70px;height:48px;transform:rotate(-18deg)"></div>
<div class="env" style="left:250px;top:3900px;width:38px;height:26px;transform:rotate(-12deg)"></div>
<div class="env" style="left:912px;top:3900px;width:38px;height:26px;transform:rotate(10deg)"></div>
<div class="env" style="left:958px;top:3930px;width:90px;height:60px;transform:rotate(14deg)"></div>
<div class="heading news-title">Join our newsletter and get<br>$20 discount for your first order</div>
<div class="abs news-form"><div class="field">Enter your email address</div><div class="go">Subscribe</div></div>

<!-- perks -->
<div class="abs perks">
  <div><svg width="12" height="12"><rect x="1" y="3" width="10" height="8" fill="none" stroke="#1f5bb4" stroke-width="1.4"/></svg>100% Money back</div>
  <div><svg width="12" height="12"><rect x="1" y="2" width="10" height="9" fill="none" stroke="#1f5bb4" stroke-width="1.4"/></svg>Non-contact shipping</div>
  <div><svg width="14" height="12"><rect x="1" y="3" width="8" height="6" fill="none" stroke="#1f5bb4" stroke-width="1.4"/><circle cx="11" cy="9" r="1.5" fill="#1f5bb4"/></svg>We deliver Country Wide</div>
</div>

<!-- footer -->
<div class="abs addr">22 Quarry Lane<br>Midrand, 1685<br><u>Show on map</u></div>
<div class="abs social"><i></i><i></i><i></i><i></i><i></i></div>
<div class="abs foot" style="left:289px;top:4178px">
  <h5>Need help</h5>
  <div class="phone"><svg width="20" height="20" viewBox="0 0 20 20"><path d="M4 2l4 1 1 4-2 2a11 11 0 004 4l2-2 4 1 1 4-3 2C9 18 2 11 2 5z" fill="none" stroke="#f58634" stroke-width="1.5"/></svg>011 555 0192</div>
  <div class="hours">Monday – Friday: 9:00-20:00<br>Saturday: 11:00 – 15:00</div>
  <div style="margin-top:30px;font-size:12px;color:var(--blue)">✉&nbsp;&nbsp;&nbsp;[email protected]</div>
</div>
<div class="abs foot" style="left:700px;top:4178px"><h5>Information</h5><ul><li>About us</li><li>Delivery information</li><li>Privacy Policy</li><li>Sales</li><li>Terms &amp; Conditions</li></ul></div>
<div class="abs foot" style="left:848px;top:4178px"><h5>Account</h5><ul><li>My account</li><li>My orders</li><li>Returns</li><li>Shipping</li><li>Wishlist</li></ul></div>
<div class="abs foot" style="left:994px;top:4178px"><h5>Store</h5><ul><li>Affiliate</li><li>Bestsellers</li><li>Discount</li><li>Latest products</li><li>Sale</li></ul></div>

<div class="abs copy">2022 © PLOVENRIK</div>
<div class="abs pay"><span>Payvo</span><span>Cardly</span><span>Debix</span><span>Walletra</span><span>Sendro</span><span>Paynest</span></div>
<div class="abs totop"><svg width="12" height="8"><path d="M1 7l5-5 5 5" fill="none" stroke="#8a93a3" stroke-width="2"/></svg></div>

</body>
</html>
```